A wine Label for a new brand of New Zealand Wine

We are looking for a Wine Label for our "Harbor Crest" brand of wines from North Otago New Zealand. We would like the label to perhaps use the HC as a logo and the rest up to the designer. We have our vineyards located in the Waitaki Valley New Zealand which is a southern region with mountains and a river flowing past our vineyard. Photos attached of Dramatic Landscape. Also attached is a basic outline of requirements for the front bottle of the label. The rear bottle label will contain writing about the wines background plus statutory regulations on Alc. Vol, bar code etc. Front Label size to be no Larger than 80mm deep by 100 mm wide. The label can be simple or graphic, whatever the designer chooses.
Target Market(s)
New Wine Brand
Look and feel
Each slider illustrates characteristics of the customer's brand and the style your logo design should communicate.

```html
<!DOCTYPE html>
<html lang="en">
<head>
<meta charset="utf-8">
<title>Harbor Crest Pinot Gris Label</title>
<link href="https://fonts.googleapis.com/css2?family=Cinzel:wght@400;700&display=swap" rel="stylesheet">
<style>
  :root {
    --page: #ffffff;
    --gold-deep: #857a1e;
    --gold-mid: #b3a23b;
    --gold-light: #d4c452;
    --gold-bright: #e8cf22;
    --gold-text: #c9ab38;
    --panel-dark: #1e1b10;
    --ink-olive: #4a4416;
    --ink-white: #ffffff;
  }
  html, body {
    margin: 0;
    padding: 0;
    width: 1200px;
    height: 1000px;
    overflow: hidden;
    background: var(--page);
  }
  .canvas {
    position: relative;
    width: 1200px;
    height: 1000px;
  }
  .wine-label {
    position: absolute;
    left: 336px;
    top: 162px;
    width: 528px;
    height: 675px;
    display: block;
  }
  .label-type {
    font-family: "Cinzel", "Times New Roman", serif;
  }
  .brand-name { fill: var(--gold-text); font-weight: 700; font-size: 80px; }
  .brand-initials { fill: var(--gold-text); font-weight: 700; font-size: 44px; }
  .varietal { fill: var(--ink-white); font-weight: 400; font-size: 25px; }
  .vintage { fill: var(--ink-white); font-family: "Times New Roman", serif; font-size: 24px; }
  .region { fill: var(--ink-olive); font-size: 15px; }
  .origin { fill: var(--ink-olive); font-size: 15px; letter-spacing: 2px; }
</style>
</head>
<body>
<main class="canvas">
  <svg class="wine-label" viewBox="0 0 528 675" xmlns="http://www.w3.org/2000/svg" role="img" aria-label="Harbor Crest Pinot Gris 2015 wine label">
    <defs>
      <linearGradient id="metal" x1="0" y1="0" x2="1" y2="0">
        <stop offset="0" stop-color="var(--gold-mid)"/>
        <stop offset="0.15" stop-color="var(--gold-deep)"/>
        <stop offset="0.35" stop-color="var(--gold-light)"/>
        <stop offset="0.5" stop-color="var(--gold-deep)"/>
        <stop offset="0.68" stop-color="var(--gold-light)"/>
        <stop offset="0.85" stop-color="var(--gold-deep)"/>
        <stop offset="1" stop-color="var(--gold-mid)"/>
      </linearGradient>
      <linearGradient id="bright-band" x1="0" y1="0" x2="1" y2="0">
        <stop offset="0" stop-color="var(--gold-bright)"/>
        <stop offset="0.3" stop-color="#a89214"/>
        <stop offset="0.55" stop-color="var(--gold-bright)"/>
        <stop offset="0.8" stop-color="#9c8712"/>
        <stop offset="1" stop-color="var(--gold-bright)"/>
      </linearGradient>
    </defs>

    <!-- metallic ground -->
    <rect class="label-ground" x="0" y="0" width="528" height="675" fill="url(#metal)"/>
    <rect class="top-band" x="0" y="0" width="528" height="20" fill="url(#bright-band)"/>
    <rect class="top-rule" x="0" y="136" width="528" height="6" fill="url(#bright-band)"/>
    <rect class="bottom-rule" x="0" y="440" width="528" height="6" fill="url(#bright-band)"/>
    <rect class="foot-band" x="0" y="615" width="528" height="60" fill="url(#bright-band)"/>
    <rect class="foot-rule" x="0" y="612" width="528" height="2" fill="var(--gold-deep)"/>

    <!-- diamond frame and dark panel -->
    <polygon class="panel-frame" points="264,24 384,142 528,142 528,440 394,440 264,578 134,440 0,440 0,142 144,142" fill="var(--gold-bright)"/>
    <polygon class="panel-dark" points="264,40 368,142 528,142 528,440 380,440 264,562 148,440 0,440 0,142 160,142" fill="var(--panel-dark)"/>

    <!-- monogram -->
    <text class="label-type brand-initials" x="264" y="122" text-anchor="middle">HC</text>

    <!-- brand name -->
    <text class="label-type brand-name" x="264" y="284" text-anchor="middle" textLength="396" lengthAdjust="spacingAndGlyphs">HARBOR</text>
    <text class="label-type brand-name" x="264" y="382" text-anchor="middle" textLength="340" lengthAdjust="spacingAndGlyphs">CREST</text>

    <!-- varietal and vintage -->
    <text class="label-type varietal" x="264" y="459" text-anchor="middle">Pinot Gris</text>
    <text class="vintage" x="264" y="489" text-anchor="middle">2015</text>

    <!-- region and origin -->
    <text class="label-type region" x="264" y="609" text-anchor="middle">Waitaki Valley - North Ortago</text>
    <text class="label-type origin" x="264" y="648" text-anchor="middle">NEW ZEALAND WINE</text>
  </svg>
</main>
</body>
</html>
```